Corporate ID design for Financial Services/Accountant Company - brochure, flyer, letterhead, email s

Hi designers :)

Torvela Financial Services requires a corporate ID design look and feel for all their ongoing items moving forward. It needs to be highly professional looking, corporate, contemporary and a standout design!

Items needed:
Letterhead design + follow-on header for 2nd and 3rd pages etc.
Tri-fold (or similar) brochure design
Flyer (A5) for mailout
Client form design
Email Signature Design

A boutique financial management company providing services in: Accounting, Bookkeeping, Payroll, Consulting services to corporate small & large clientele in Australia. The design needs to run across all items, matching them together to communicate professionalism, finance and style.

Logo needs to be on all items, however the design across all items can be completely different as long as it works in the logo (i.e don't want footprints over whole designs as it doesn't communicate hi-end corporate feel).

Would like a beautifully designed graphic element/design style included across all items to match together and become part of the corporate identity/branding.

Fresh, clean, modern, corporate and professional style.

ITEMS - how they will be used>
Letterhead - Will be used mainly online so design needs to be able to go into WORD document to edit over.

A5 flyer - will be printed on high gloss card. Needs to be double sided full colour for print with 3mm bleed

Tri-fold brochure - will be printed as well, needs to be standard print size, full cmyk colour both sides and it will be handed out to new clients for more information on prices & staff etc

Email signature - Just a nice simple and clean design with matching element from above items.

Client Form - needs to be laid out with a nice design in indesign please.

Thanks & look forward to your submissions!

Target Market(s)

Target market is professional businesses wanting financial and bookkeeping services delivered with exceptional service.

Industry/Entity Type

Financial

Requirements
Must have
• Logo
• Work in corporate/logo colours.
• Would like final files created in indesign if possible please. Graphics and illustration are fine in illustrator first.
• Design with some or a element from website to match everything together>
• http://www.torvela.com.au/
Nice to have
• Would love to see some designs in the blue, with creative designs/illustrations in background watermark (i.e opacity of grey showing a hint of a design across all items)
• Could work in the orange from website text if it looks good on some areas.
Should not have
• Don't want footprints over all items as the whole design. We want a new creative look and feel (corporate & professional) but just working in the logo. Can include PARTS of the footprint &/or logo in design across items.

```html
<!DOCTYPE html>
<html lang="en">
<head>
<meta charset="utf-8">
<title>Torvela Financial Services — Letterhead</title>
<link rel="stylesheet" href="https://fonts.googleapis.com/css2?family=Noto+Serif:wght@400;700&display=swap">
<style>
  :root {
    --paper: #ffffff;
    --brand-blue: #15679c;
    --ink-grey: #5a5a5a;
    --faint-grey: rgba(225, 225, 225, 0.85);
    --faint-grey-soft: rgba(225, 225, 225, 0.4);
    --on-blue: #ffffff;
  }
  html, body {
    margin: 0;
    padding: 0;
    overflow: hidden;
    background: var(--paper);
  }
  .letterhead {
    position: relative;
    width: 848px;
    height: 1200px;
    background: var(--paper);
    overflow: hidden;
    font-family: "Noto Serif", Georgia, serif;
  }
  .brand {
    position: absolute;
    left: 57px;
    top: 40px;
    margin: 0;
    font-weight: 400;
    color: var(--ink-grey);
  }
  .brand-name {
    display: flex;
    align-items: flex-start;
    gap: 10px;
    font-size: 46px;
    line-height: 60px;
    letter-spacing: 0.04em;
  }
  .brand-mark {
    width: 14px;
    height: 14px;
    margin-top: 6px;
    border-radius: 50%;
    background: var(--brand-blue);
  }
  .brand-tagline {
    display: block;
    margin-top: 10px;
    font-size: 14px;
    line-height: 18px;
    letter-spacing: 0.24em;
    text-transform: uppercase;
  }
  .watermark-trail {
    position: absolute;
    left: 50px;
    top: 600px;
    width: 320px;
    height: 470px;
    background: radial-gradient(ellipse closest-side at 50% 50%, var(--faint-grey) 0%, var(--faint-grey-soft) 55%, rgba(255,255,255,0) 100%);
  }
  .footer-wave {
    position: absolute;
    left: 0;
    bottom: 0;
    width: 848px;
    height: 180px;
    display: block;
  }
  .contact-block {
    position: absolute;
    right: 31px;
    top: 1062px;
    margin: 0;
    font-style: normal;
    text-align: right;
    font-size: 15.5px;
    line-height: 21.5px;
    color: var(--on-blue);
  }
  .contact-block .web {
    font-weight: 700;
  }
</style>
</head>
<body>
  <main class="letterhead">
    <h1 class="brand">
      <span class="brand-name">Torvela<span class="brand-mark"></span></span>
      <span class="brand-tagline">Financial Services</span>
    </h1>

    <div class="watermark-trail" role="img" aria-label="Faint grey brand trail motif running diagonally up the page"></div>

    <svg class="footer-wave" viewBox="0 1020 848 180" preserveAspectRatio="none" aria-hidden="true">
      <path d="M0 1085 C 90 1128, 200 1118, 400 1080 S 760 1028, 848 1036 L 848 1200 L 0 1200 Z" fill="var(--brand-blue)"/>
    </svg>

    <address class="contact-block">
      Daniel Harlow, Director<br>
      Northbay LPO&nbsp; PO Box 7<br>
      NSW&nbsp; 2099<br>
      ABN 12 345 678 901<br>
      <span class="web">www.torvela.com.au</span>
    </address>
  </main>
</body>
</html>
```